Spiritual Support flyer design

I offer a range of spiritual support options from a drop in group to meditation. I work alone in two locations, one at home and the other in the local town centre therapy centre. I do not want people to be confused about where to go for each item so thought one side could be the town centre group and the other side of the leaflet could be the things I offer from home. I need to find a way to present a list of things I do and make it look inviting so people want to contact me. I want it to feel inspirational, uplifting, light hearted, with a gentle feel of support or coming home to somewhere safe. The leaflet needs to look eye catching as it will be where there are many other leaflets the same size (A5). I love purples, as they tend to be spiritual colours or the look below of light bursting through the clouds seems appropriate picture wise. I do not have a logo.
The title can be Quiet Harbour. On one side I would like to introduce a Spiritual Experiences drop-in group held at the Larkfield Centre, Colchester 1-2pm every four weeks to share spiritual experiences with others. I can give you more words for that when you are ready. The other side needs to feature the things I offer from my own home which are: Spiritual Counselling, Private email guidance, Meditation one to one, and Quiet Harbour Days, which are like a days retreat. It might be a good idea to mention prices but not in an obvious way, so have that just readable in small print.

Town

```html
<!DOCTYPE html>
<html lang="en">
<head>
<meta charset="utf-8">
<title>Spiritual Experiences – Drop-in Group Flyer</title>
<link rel="stylesheet" href="https://fonts.googleapis.com/css2?family=Open+Sans:wght@300;400;700&family=PT+Sans:wght@400;700&family=PT+Sans+Narrow:wght@400;700&family=Cormorant+Garamond:wght@500;700&display=swap">
<style>
  :root {
    --page-bg: #e9e7ea;
    --paper: #ffffff;
    --purple: #6a2b9c;
    --purple-deep: #5a1f86;
    --accent-orange: #f5a21b;
    --ink: #1c1c1c;
    --soft-grey: #8a8a8a;
    --contact-pink: #ee4a72;
    --white: #ffffff;
  }
  * { margin: 0; padding: 0; box-sizing: border-box; }
  html, body {
    width: 1165px; height: 1200px; overflow: hidden;
    background: var(--page-bg);
  }
  .flyer {
    position: absolute; left: 173px; top: 20px;
    width: 818px; height: 1160px;
    background: var(--paper);
    border-top: 5px solid var(--purple);
    overflow: hidden;
    font-family: "Open Sans", sans-serif;
  }
  .hero-photo {
    position: absolute; left: 0; top: 505px; width: 100%; height: 655px;
    background:
      linear-gradient(180deg,
        rgba(255,255,255,1) 0%,
        rgba(252,238,232,1) 14%,
        rgba(246,214,210,1) 30%,
        rgba(236,190,196,1) 45%,
        rgba(214,170,196,1) 55%,
        rgba(120,60,150,1) 64%,
        rgba(96,38,140,1) 72%,
        rgba(150,96,180,1) 84%,
        rgba(108,52,150,1) 100%);
  }
  .hero-photo::after {
    content: ""; position: absolute; left: 340px; top: 330px;
    width: 110px; height: 325px;
    background: radial-gradient(ellipse at center, rgba(255,250,235,0.95) 0%, rgba(255,240,220,0.5) 45%, rgba(255,240,220,0) 75%);
  }
  .intro {
    position: absolute; left: 73px; top: 67px; width: 300px;
    font-size: 28px; line-height: 24.5px; font-weight: 300; color: var(--soft-grey);
    letter-spacing: -0.2px;
  }
  .intro strong, .bio-name { font-family: "PT Sans", sans-serif; font-weight: 700; color: var(--ink); }
  .invitation {
    position: absolute; left: 412px; top: 67px; width: 345px;
    font-family: "PT Sans Narrow", sans-serif; font-size: 27px; line-height: 31px;
    color: var(--purple);
  }
  .title-block {
    position: absolute; left: 0; top: 324px; width: 101px; height: 160px;
    background: var(--purple);
  }
  .title-stripe {
    position: absolute; left: 105px; top: 324px; width: 6px; height: 160px;
    background: var(--accent-orange);
  }
  .title { position: absolute; left: 0; top: 310px; }
  .title text { font-family: "Cormorant Garamond", serif; fill: var(--purple); }
  .bio {
    position: absolute; top: 528px;
    font-weight: 300; color: var(--soft-grey);
  }
  .bio--mara { left: 73px; width: 300px; font-size: 28px; line-height: 27px; }
  .bio--jo { left: 412px; width: 340px; font-size: 30px; line-height: 35px; }
  .bio-name { font-size: 29px; }
  .contact-call {
    position: absolute; left: 73px; top: 750px; width: 300px;
    font-family: "PT Sans Narrow", sans-serif; font-weight: 700;
    font-size: 47px; line-height: 47px; color: var(--contact-pink);
  }
  .contact-details {
    position: absolute; left: 73px; top: 924px;
    font-family: "PT Sans", sans-serif; color: var(--white); font-weight: 700;
  }
  .contact-email { font-size: 31px; line-height: 36px; }
  .contact-phone { font-size: 55px; line-height: 58px; }
  .venue {
    position: absolute; left: 73px; top: 1030px;
    font-family: "PT Sans", sans-serif; font-size: 24px; line-height: 27px; color: var(--white);
  }
  .contribution {
    position: absolute; right: 73px; top: 1030px; text-align: right;
    font-family: "PT Sans", sans-serif; font-weight: 700; color: var(--white);
  }
  .contribution-label { font-size: 28px; line-height: 34px; }
  .contribution-price { font-size: 40px; line-height: 44px; }
</style>
</head>
<body>
  <main class="flyer">
    <div class="hero-photo" role="img" aria-label="Photo of two cupped hands raised towards a glowing sunset over a lake"></div>

    <p class="intro"><strong>Mara and Jo</strong> invite you to drop in and share any spiritual experiences you may have had, enlightened moments, or developing spiritual gifts, in a supportive environment.</p>

    <p class="invitation">Perhaps you feel that you are the only one experiencing what you do and would like to talk about it, or listen to others experiences.<br>In the group you can share with like-minded souls for personal development and inspiration.</p>

    <div class="title-block"></div>
    <div class="title-stripe"></div>
    <svg class="title" width="818" height="180" viewBox="0 0 818 180" aria-label="Spiritual Experiences">
      <text x="132" y="97" font-size="112" font-weight="500" textLength="611" lengthAdjust="spacingAndGlyphs">SPIRITUAL</text>
      <text x="138" y="165" font-size="78" font-weight="700" textLength="605" lengthAdjust="spacingAndGlyphs">EXPERIENCES</text>
    </svg>

    <p class="bio bio--mara"><span class="bio-name">Mara Vell</span> – has loved all things spiritual from an early age and provides email consultations, spiritual counselling, and Quiet Harbour days</p>

    <p class="contact-call">Please contact Mara for future dates.</p>

    <p class="bio bio--jo"><span class="bio-name">Jo Harlow</span> – had a spiritual awakening and became open to angels, is sensitive to energies, and has been on a pathway of self-discovery ever since. She enjoys emotionally supporting others on their life journey.</p>

    <div class="contact-details">
      <p class="contact-email">Mara.vell@brightmail.co.uk</p>
      <p class="contact-phone">01632 960417</p>
    </div>

    <p class="venue">A drop-in group at<br>The Larkfield Centre,<br>8 Mercer Lane, Colchester</p>

    <div class="contribution">
      <p class="contribution-label">Contribution</p>
      <p class="contribution-price">£5</p>
    </div>
  </main>
</body>
</html>
```